"Velmaro" sparkling beverage

Dear All!
I need a stick label (82*95 - front label, 82*65 - back label )design for а sparkling beverage, name is "Velmaro", 4 flavours: lemonade,duchess pear, estragon, original. Transparent glass bottles 0,5 liter (alumnium closure 28*15)/0,33 liter (crown cap), neck label should also be on the bottle 0,5 liter.
European style is welcomed
Do not send the disigns with a little changes several times, please!!!
Young people from 12-30 ages old

```html
<!DOCTYPE html>
<html lang="en">
<head>
<meta charset="utf-8">
<title>Velmaro sparkling beverage labels</title>
<link rel="stylesheet" href="https://fonts.googleapis.com/css2?family=Didact+Gothic&display=swap">
<style>
  :root {
    --page-bg: #f2ece0;
    --label-bg: #93eef0;
    --brand-green: #4a9a1c;
    --tagline-green: #2f7a10;
    --flavour-orange: #f0a01a;
  }
  * { margin: 0; padding: 0; box-sizing: border-box; }
  html, body {
    width: 846px;
    height: 1200px;
    overflow: hidden;
    background: var(--page-bg);
  }
  .canvas {
    width: 846px;
    height: 1200px;
    display: flex;
    flex-direction: row;
    align-items: center;
    justify-content: center;
    gap: 24px;
  }
  .label {
    position: relative;
    width: 370px;
    height: 428px;
    background: var(--label-bg);
    box-shadow: 0 1px 3px rgba(0,0,0,0.12);
  }
  .label__art {
    position: absolute;
    inset: 0;
    width: 100%;
    height: 100%;
  }
  .label__flavour,
  .label__brand,
  .label__tagline {
    position: absolute;
    left: 0;
    right: 0;
    text-align: center;
    font-family: "Didact Gothic", sans-serif;
    font-weight: 400;
    line-height: 1;
    white-space: nowrap;
  }
  .label__flavour {
    top: 170px;
    color: var(--flavour-orange);
    font-size: 24px;
    letter-spacing: 1px;
  }
  .label__brand {
    top: 193px;
    color: var(--brand-green);
    font-size: 50px;
    letter-spacing: 1px;
  }
  .label__tagline {
    top: 240px;
    color: var(--tagline-green);
    font-size: 15px;
    letter-spacing: 0.3px;
  }
</style>
</head>
<body>
<main class="canvas">

  <section class="label label--lemonade">
    <svg class="label__art" viewBox="0 0 370 428">
      <defs>
        <radialGradient id="lemon-fill" cx="50%" cy="50%" r="50%">
          <stop offset="0%" stop-color="#f7d23a"/>
          <stop offset="60%" stop-color="#f3b72a"/>
          <stop offset="100%" stop-color="#6aa23a"/>
        </radialGradient>
      </defs>
      <path role="img" aria-label="Circular arrangement of lemons, orange slices, leaves and ice cubes, upper half"
            d="M35 166 A155 176 0 0 1 335 166 Z" fill="url(#lemon-fill)" opacity="0.9"/>
      <path role="img" aria-label="Circular arrangement of lemons, orange slices, leaves and ice cubes, lower half"
            d="M36 262 A155 176 0 0 0 334 262 Z" fill="url(#lemon-fill)" opacity="0.9"/>
    </svg>
    <p class="label__flavour">lemonade</p>
    <h1 class="label__brand">VELMARO</h1>
    <p class="label__tagline">sparkling beverage</p>
  </section>

  <section class="label label--pear">
    <svg class="label__art" viewBox="0 0 370 428">
      <defs>
        <radialGradient id="pear-fill" cx="50%" cy="50%" r="50%">
          <stop offset="0%" stop-color="#efe6cf"/>
          <stop offset="55%" stop-color="#b9c16a"/>
          <stop offset="100%" stop-color="#5e9a3a"/>
        </radialGradient>
      </defs>
      <path role="img" aria-label="Circular arrangement of whole and halved duchess pears, leaves and ice cubes, upper half"
            d="M35 166 A155 176 0 0 1 335 166 Z" fill="url(#pear-fill)" opacity="0.9"/>
      <path role="img" aria-label="Circular arrangement of whole and halved duchess pears, leaves and ice cubes, lower half"
            d="M36 262 A155 176 0 0 0 334 262 Z" fill="url(#pear-fill)" opacity="0.9"/>
    </svg>
    <p class="label__flavour">duchess pear</p>
    <h2 class="label__brand">VELMARO</h2>
    <p class="label__tagline">sparkling beverage</p>
  </section>

</main>
</body>
</html>
```